Visitenkarten-Design für Bewertung von Grundstücken
Zielgruppe
Ich bin Sachverständige für die Bewertung von bebauten und unbebauten Grundstücken und erstelle Verkehrswertgutachten für (überwiegend) Sylter Immobilien. Meine Zielgruppe sind die Eigentümer dieser Immobilien, die aus verschiedensten Gründen eine Wertermittlung für ihre Immobilie benötigen, z.B. wegen
steuerlichen Anlässen (Erbschaft, Übertragung, Schenkung)
Erbauseinandersetzungen / Pflichtteilsansprüchen
Ehescheidung
Kauf oder Verkauf eines Grundstücks
Vermögensaufstellung
Vormundschaftsangelegenheiten
Bewertung von Rechten und Belastungen (Wohnrecht, Nießbrauch, Erbbaurecht)
Aufgabenstellung
Ich habe mir erst kürzlich eine kleine Homepage erstellen lassen, die mir sehr gut gefällt.
www.wertgutachten-haldorf.de
Das Design der Visitenkarte sollte dazu passen und prägnant und schnörkellos sein. Mein Logo mit der Lupe sollte sich dort wiederfinden, ebenfalls die Farben. Ich bevorzuge schlichte Eleganz, eine schöne Haptik, hochwertiges Papier, evtl mit Prägedruck, da bin ich aber noch unsicher, evtl. eine matte und eine Hochglanzseite....

```html
<!DOCTYPE html>
<html lang="de">
<head>
<meta charset="utf-8">
<title>Visitenkarte – Sachverständigenbüro Haldorf</title>
<link href="https://fonts.googleapis.com/css2?family=Barlow:wght@300;400;600;700&display=swap" rel="stylesheet">
<style>
  :root {
    --stage: #c9c9c9;
    --card: #67686d;
    --card-light: #74757a;
    --sage: #a9bd9f;
    --white: #f4f4f2;
    --muted: #d9dadc;
    --strip: #ececea;
    --strip-dark: #8a8b8f;
  }
  * { margin: 0; padding: 0; box-sizing: border-box; }
  html, body { width: 1200px; height: 900px; overflow: hidden; }
  body {
    background: var(--stage);
    font-family: "Barlow", sans-serif;
    display: flex;
    align-items: center;
    justify-content: center;
    gap: 40px;
  }
  .card {
    width: 540px;
    height: 350px;
    background: var(--card);
    position: relative;
    overflow: hidden;
    box-shadow: 0 12px 30px rgba(0,0,0,0.18);
  }
  /* Front side */
  .pattern-strip {
    position: absolute;
    top: 0; bottom: 0;
    width: 62px;
    background: linear-gradient(180deg, var(--strip), #dcdcda);
  }
  .pattern-strip.left { left: 0; }
  .pattern-strip.right { right: 0; }
  .brand-square {
    position: absolute;
    left: 228px; top: 0;
    width: 84px; height: 84px;
    background: var(--sage);
  }
  .front-title {
    position: absolute;
    left: 62px; right: 62px; top: 104px;
    text-align: center;
    line-height: 1.15;
  }
  .office {
    color: var(--white);
    font-weight: 400;
    font-size: 21px;
    letter-spacing: 0.5px;
    text-transform: uppercase;
  }
  .owner {
    color: var(--sage);
    font-weight: 400;
    font-size: 21px;
    letter-spacing: 0.5px;
    text-transform: uppercase;
  }
  .details {
    position: absolute;
    left: 62px; right: 62px; top: 196px;
    display: flex;
    justify-content: center;
    align-items: center;
    gap: 30px;
  }
  .person-name {
    color: var(--sage);
    font-weight: 700;
    font-size: 17px;
  }
  .person-role {
    color: var(--muted);
    font-weight: 300;
    font-size: 13px;
  }
  .divider {
    width: 1px; height: 46px;
    background: var(--sage);
  }
  .contact {
    color: var(--muted);
    font-weight: 300;
    font-size: 13px;
    line-height: 1.5;
  }
  .website {
    position: absolute;
    left: 62px; right: 62px; bottom: 42px;
    text-align: center;
    color: var(--white);
    font-weight: 700;
    font-size: 14px;
  }
  /* Back side */
  .card.back {
    background: radial-gradient(circle at 50% 50%, var(--card-light), var(--card));
    display: flex;
    align-items: center;
    justify-content: center;
  }
  .back-title { line-height: 1.15; }
</style>
</head>
<body>
  <section class="card front">
    <div class="pattern-strip left" role="img" aria-label="Dekoratives Muster aus dem Büro-Symbol"></div>
    <div class="pattern-strip right" role="img" aria-label="Dekoratives Muster aus dem Büro-Symbol"></div>
    <div class="brand-square"></div>
    <div class="front-title">
      <p class="office">Sachverständigenbüro Haldorf</p>
      <p class="owner">Marlene Haldorf</p>
    </div>
    <div class="details">
      <div class="person">
        <p class="person-name">Marlene Haldorf</p>
        <p class="person-role">Immobilienbewerter</p>
      </div>
      <div class="divider"></div>
      <div class="contact">
        <p>+49 151 20 38 417</p>
        <p>kontakt@wertgutachten-haldorf.de</p>
      </div>
    </div>
    <p class="website">www.wertgutachten-haldorf.de</p>
  </section>

  <section class="card back">
    <div class="back-title">
      <p class="office">Sachverständigenbüro Haldorf</p>
      <p class="owner">Marlene Haldorf</p>
    </div>
  </section>
</body>
</html>
```